A Real Estate Company Needs a Business Card Design

We need a business card design for a new company based in Boston MA called "Brackenfield Real Estate LLC" we are a small company but we like a big corporate look, a simple, sleek, modern and progressive look. we would like the option of having a design that could include the real estate agents personal photo and also a design if the realtor decides not to have a photo. we do not have LOGO at this moment, please use any property look pic corporate with word" Brackenfield Real Estate LLC" please see attached file as an example.
Industry/Entity Type
Business

```html
<!DOCTYPE html>
<html lang="en">
<head>
<meta charset="utf-8">
<title>Brackenfield Real Estate LLC – Business Card</title>
<link rel="stylesheet" href="https://fonts.googleapis.com/css2?family=Hind:wght@400;500;600&display=swap">
<style>
  :root {
    --backdrop: #dedede;
    --card-white: #ffffff;
    --brand-blue: #1d6fbd;
    --deep-blue: #22479d;
    --mid-blue: #1478c6;
    --sky-blue: #5ec2ef;
    --rule-grey: #9b9fa5;
    --ink: #1f1f1f;
  }
  * { margin: 0; padding: 0; box-sizing: border-box; }
  html, body {
    width: 1200px;
    height: 1058px;
    overflow: hidden;
    background: var(--backdrop);
    font-family: "Hind", Arial, sans-serif;
  }
  .stage { position: relative; width: 1200px; height: 1058px; }

  .card {
    position: absolute;
    width: 620px;
    height: 376px;
    overflow: hidden;
    box-shadow: 0 2px 4px rgba(0,0,0,0.18);
  }
  .card--front { left: 236px; top: 162px; background: var(--card-white); }
  .card--back {
    left: 234px; top: 567px;
    background: linear-gradient(180deg, var(--deep-blue) 0%, var(--mid-blue) 50%, #1f56ab 100%);
  }

  .card__band {
    position: absolute;
    left: 0; right: 0; top: 0;
    height: 34px;
    background: linear-gradient(90deg, var(--sky-blue) 0%, var(--brand-blue) 100%);
  }
  .card__rule {
    position: absolute;
    left: 0; right: 0; top: 40px;
    height: 4px;
    background: var(--rule-grey);
  }

  .wordmark {
    position: absolute;
    display: flex;
    align-items: center;
    gap: 12px;
    font-weight: 600;
    font-size: 30px;
    line-height: 1;
    white-space: nowrap;
  }
  .wordmark__square { width: 26px; height: 26px; flex: none; }
  .card--front .wordmark { left: 56px; top: 118px; color: var(--brand-blue); }
  .card--front .wordmark__square { background: var(--brand-blue); }
  .card--back .wordmark { left: 0; right: 0; top: 174px; justify-content: center; color: #fff; }
  .card--back .wordmark__square { background: #fff; }

  .holder { position: absolute; left: 52px; top: 286px; color: var(--ink); }
  .holder__name { font-size: 21px; font-weight: 500; line-height: 1.1; }
  .holder__role { font-size: 16px; font-style: italic; margin-top: 4px; }

  .contact { position: absolute; left: 276px; top: 229px; list-style: none; color: var(--ink); font-size: 18px; line-height: 26px; }
  .contact__item { display: flex; align-items: flex-start; gap: 6px; }
  .contact__icon { width: 14px; height: 16px; margin-top: 5px; flex: none; }
  .contact__text { display: block; }
</style>
</head>
<body>
<main class="stage">

  <section class="card card--front" aria-label="Business card front">
    <div class="card__band"></div>
    <div class="card__rule"></div>

    <div class="wordmark"><span class="wordmark__square"></span>Brackenfield Real Estate LLC</div>

    <div class="holder">
      <p class="holder__name">Nora Whitcombe</p>
      <p class="holder__role">President</p>
    </div>

    <ul class="contact">
      <li class="contact__item">
        <svg class="contact__icon" viewBox="0 0 14 16" aria-hidden="true"><path d="M7 1 C3.7 1 1.5 3.4 1.5 6.2 C1.5 9.5 7 15 7 15 C7 15 12.5 9.5 12.5 6.2 C12.5 3.4 10.3 1 7 1 Z" fill="var(--brand-blue)"/><circle cx="7" cy="6" r="2" fill="#fff"/></svg>
        <span class="contact__text">48 Alder Lane,<br>Medford, MA 02155</span>
      </li>
      <li class="contact__item">
        <svg class="contact__icon" viewBox="0 0 14 16" aria-hidden="true"><rect x="3" y="1" width="8" height="14" rx="1.5" fill="var(--brand-blue)"/><rect x="4.5" y="3" width="5" height="6" fill="#fff"/></svg>
        <span class="contact__text">(617) 555-0138</span>
      </li>
      <li class="contact__item">
        <svg class="contact__icon" viewBox="0 0 14 16" aria-hidden="true"><rect x="1" y="4" width="12" height="9" fill="none" stroke="var(--brand-blue)" stroke-width="1.6"/><path d="M1 4 L7 9 L13 4" fill="none" stroke="var(--brand-blue)" stroke-width="1.6"/></svg>
        <span class="contact__text">contact@brackenfieldrealestate.com</span>
      </li>
    </ul>
  </section>

  <section class="card card--back" aria-label="Business card back">
    <div class="wordmark"><span class="wordmark__square"></span>Brackenfield Real Estate LLC</div>
  </section>

</main>
</body>
</html>
```